Wordpress template for a mens-choire webpage

Task is to design a Wordpress template for an 98 years old estonian mens choire webpage.
Design should involve details from the attached files, choire logo and the colors of the choire flag: in horizontal orientation bright sky-blue, white, bright grass-green.
Designer signature is allowed to be added to the template, with country of origin.

Thank you everyone for your great designs!
Our project has now entered into a voting and decision phase until 14th of March 2014 (included).

```html
<!DOCTYPE html>
<html lang="en">
<head>
<meta charset="utf-8">
<title>Estonian Mens Choire</title>
<link href="https://fonts.googleapis.com/css2?family=Bebas+Neue&family=Roboto:wght@400;500;700&display=swap" rel="stylesheet">
<style>
:root{
  --green:#12b13c;
  --green-dark:#0e9a33;
  --red:#a8141c;
  --blue:#1a6fc4;
  --text:#555;
  --grey:#e4e4e4;
  --white:#fff;
}
*{margin:0;padding:0;box-sizing:border-box}
html,body{width:826px;height:1200px;overflow:hidden}
body{position:relative;font-family:'Roboto',sans-serif;background:#f1f1f1;color:var(--text)}
.abs{position:absolute}
.hero-band{left:0;top:0;width:826px;height:432px;background:var(--green)}
.header{left:90px;top:20px;width:645px;height:69px;background:var(--white);box-shadow:0 1px 3px rgba(0,0,0,.2)}
.call{left:22px;top:14px;font-size:9px;color:#777;display:flex;align-items:center;gap:4px}
.call strong{font-size:13.5px;color:var(--red);font-weight:500;margin-left:2px}
.search{left:468px;top:10px;width:153px;height:22px;border:1px solid #ddd;display:flex}
.search span{flex:1;font-size:7px;color:#bbb;padding:7px 6px}
.search i{width:26px;border-left:1px solid #ddd;display:flex;align-items:center;justify-content:center}
.nav{left:0;top:41px;width:645px;height:28px;background:linear-gradient(#fafafa,#e2e2e2);border-top:1px solid #e5e5e5}
.nav a{position:absolute;top:8px;font-size:11.5px;color:#555;text-decoration:none}
.nav a.active{color:var(--red)}
.brand{left:386px;top:24px;width:54px;height:54px;border-radius:50%;background:var(--white);border:2px solid var(--green);display:flex;align-items:center;justify-content:center;font-size:9px;font-weight:500;color:var(--red)}
.slider{left:90px;top:110px;width:645px;height:258px;background:var(--white);box-shadow:0 1px 4px rgba(0,0,0,.2)}
.slide-photo{left:7px;top:6px;width:632px;height:245px;background:linear-gradient(180deg,#8c9096 0%,#c7cacd 45%,#a39b8c 75%,#8b8276 100%)}
.headline{left:144px;top:203px;font-family:'Bebas Neue',sans-serif;line-height:1}
.headline .l1{font-size:32px;color:var(--green)}
.headline .l2{font-size:42px;color:var(--red);margin-top:2px}
.rule{left:144px;top:285px;width:256px;height:2px;background:var(--red)}
.arrow{width:29px;height:29px;border-radius:50%;background:#555;border:3px solid var(--white);top:224px;display:flex;align-items:center;justify-content:center}
.quote{left:90px;top:384px;width:650px;color:var(--white);font-size:9px;line-height:19px;padding-left:19px}
.quote b{position:absolute;left:0;top:0;font-size:15px}
h2{font-weight:400;color:var(--red);font-size:14.5px}
p.body{font-size:9px;line-height:19px;color:var(--text)}
.link{font-size:10px;color:var(--green)}
.btn{background:var(--green);color:var(--white);font-size:9.5px;display:flex;align-items:center;justify-content:center;border-radius:2px;box-shadow:0 1px 0 var(--green-dark)}
.ph{background:linear-gradient(135deg,#6b5f57,#2d2a2a)}
.prog{left:527px;width:207px;height:96px}
.prog .ph{position:absolute;left:3px;top:0;width:79px;height:68px;border:2px solid var(--white);box-shadow:0 0 2px rgba(0,0,0,.3)}
.prog .date{position:absolute;left:91px;top:2px;font-size:9px;color:var(--red);font-weight:500}
.prog .txt{position:absolute;left:90px;top:14px;width:120px;font-size:8px;line-height:15.5px;color:#555}
.prog .txt em{font-style:normal;color:var(--green);font-weight:500;margin-left:6px}
.dots{height:0;border-top:1px dotted #bbb}
.line{height:1px;background:#ddd}
.gal{top:794px;width:130px;height:109px;border-radius:3px}
.footer{left:0;top:946px;width:826px;height:254px;background:var(--blue);color:var(--white)}
.footer h3{position:absolute;font-weight:400;font-size:12px;letter-spacing:.3px}
.footer h3::after{content:"";position:absolute;left:0;top:19px;width:38px;height:2px;background:var(--white)}
.thumb{width:44px;height:42px;background:linear-gradient(135deg,#b8463a,#2b2b4a)}
.tweet{left:261px;font-size:8px;line-height:12px;padding-left:14px}
.tweet .t{color:#5fe27d}
.tweet svg{position:absolute;left:0;top:2px}
.show{left:592px;font-size:8px;line-height:12px}
.show .ph{position:absolute;left:0;top:-6px;width:45px;height:35px;border:2px solid var(--white)}
.show div.t{position:absolute;left:57px;top:0;white-space:nowrap}
.social{top:1167px;width:20px;height:20px;border-radius:50%;background:var(--white)}
</style>
</head>
<body>
<div class="abs hero-band"></div>

<header class="abs header">
  <div class="abs call">
    <svg width="8" height="8" viewBox="0 0 10 10"><path d="M2 1l2 2-1 1.5c.7 1.3 1.5 2.1 2.5 2.5L7 6l2 2-1.5 1.5C4.5 9 1 5.5.5 2.5z" fill="#e07b1a"/></svg>
    Call Us: <strong>(030) 55 01 23 45</strong>
  </div>
  <div class="abs search"><span>Enter any Keywords...</span><i><svg width="10" height="10" viewBox="0 0 10 10"><circle cx="4" cy="4" r="3" fill="none" stroke="#d9a13a" stroke-width="1.4"/><path d="M6 6l3 3" stroke="#d9a13a" stroke-width="1.6"/></svg></i></div>
  <nav class="abs nav">
    <a class="active" style="left:22px">Home</a>
    <a style="left:105px">About Us</a>
    <a style="left:193px">Programs</a>
    <a style="left:399px">Events</a>
    <a style="left:483px">Gallery</a>
    <a style="left:566px">Contact Us</a>
  </nav>
</header>
<div class="abs brand">Laulukoor</div>

<section class="abs slider">
  <div class="abs slide-photo" role="img" aria-label="Choir singers in black tuxedos standing in a long line on a beach under a grey sky"></div>
</section>
<div class="abs headline"><div class="l1">98 Years of</div><div class="l2">Estonian Choire</div></div>
<div class="abs rule"></div>
<div class="abs arrow" style="left:82px"><svg width="10" height="12" viewBox="0 0 10 12"><path d="M7 1L2 6l5 5" fill="none" stroke="#fff" stroke-width="2"/></svg></div>
<div class="abs arrow" style="left:718px"><svg width="10" height="12" viewBox="0 0 10 12"><path d="M3 1l5 5-5 5" fill="none" stroke="#fff" stroke-width="2"/></svg></div>

<blockquote class="abs quote"><b>&ldquo;</b>Sed ut perspiciatis unde omnis iste natus error sit voluptatem accusantium doloremque lghgjdgjhkjh,audantium, totam rem aperiam, eaque ipsa quae abhf llo inventore veritatis et quasi architecto beatae vitae dicta sunt explicabo. .................. <b style="position:static;font-size:13px">&rdquo;</b></blockquote>

<h2 class="abs" style="left:89px;top:448px">Welcome To Estonian Mens Choire</h2>
<p class="abs body" style="left:90px;top:481px;width:420px">"Lorem ipsum dolor sit amet, consectetur adipisicing elit, sed do eiusmod tempor incididunt ut labore e magna aliqua. Ut enim ad minim veniam, quis nostrud exercitation ullamco........</p>
<p class="abs body" style="left:90px;top:529px;width:420px">Aboris nisi ut aliquip ex ea coconsequat. Duis aute irure dolor in reprehenderit in voluptate velit esse ci dolore eu fugiat nulla pariExcepteur sint occaecat cupidatat non proident............</p>
<div class="abs link" style="left:90px;top:569px">Read More</div>

<h2 class="abs" style="left:89px;top:594px">Our Latest Video</h2>
<div class="abs ph" style="left:91px;top:627px;width:230px;height:128px" role="img" aria-label="Video still of musicians rehearsing with violins and a grand piano"></div>
<svg class="abs" style="left:200px;top:684px" width="12" height="14" viewBox="0 0 12 14"><path d="M1 1l10 6-10 6z" fill="#fff"/></svg>
<div class="abs" style="left:338px;top:640px;font-size:10px;color:var(--red);font-weight:500">Similique sunt in culpa qui officia</div>
<p class="abs body" style="left:338px;top:658px;width:170px;font-size:8px;line-height:17.5px">Lorhjbgem ipsum dolor sit a met, consectetur magna aliqua. Ut enim ad mdginim veniam,lo quis nostrud exercitation ullam.lorem......</p>
<div class="abs btn" style="left:335px;top:716px;width:69px;height:18px">Watch Now!</div>

<h2 class="abs" style="left:527px;top:449px">Latest Programs</h2>
<div class="abs line" style="left:527px;top:468px;width:207px"></div>
<svg class="abs" style="left:714px;top:452px" width="21" height="9" viewBox="0 0 21 9"><circle cx="4.5" cy="4.5" r="4.5" fill="#12b13c"/><circle cx="15.5" cy="4.5" r="4.5" fill="#12b13c"/><path d="M5.5 2.5l-2 2 2 2M14.5 2.5l2 2-2 2" fill="none" stroke="#fff" stroke-width="1.2"/></svg>

<div class="abs prog" style="top:482px"><div class="ph" role="img" aria-label="Choir group portrait in rows"></div><div class="date">12/12/2013</div><div class="txt">Lorem ipsum dolor sit amet, co nsectetur adipisicing elit, sed do eiusmod tempor incididunt ut la bore ................. <em>Read More</em></div></div>
<div class="abs dots" style="left:527px;top:565px;width:207px"></div>
<div class="abs prog" style="top:578px"><div class="ph" role="img" aria-label="Singer in tuxedo in front of the choir"></div><div class="date">12/12/2013</div><div class="txt">Lorem ipsum dolor sit amet, co nsectetur adipisicing elit, sed do eiusmod tempor incididunt ut la bore ................. <em>Read More</em></div></div>
<div class="abs dots" style="left:527px;top:661px;width:207px"></div>
<div class="abs prog" style="top:674px"><div class="ph" role="img" aria-label="Festival parade in folk costumes"></div><div class="date">12/12/2013</div><div class="txt">Lorem ipsum dolor sit amet, co nsectetur adipisicing elit, sed do eiusmod tempor incididunt ut la bore ................. <em>Read More</em></div></div>
<div class="abs dots" style="left:527px;top:756px;width:207px"></div>

<div class="abs line" style="left:89px;top:773px;width:646px"></div>
<h2 class="abs" style="left:89px;top:791px">Gallery</h2>
<p class="abs body" style="left:89px;top:810px;width:200px;font-size:8.5px;line-height:17.5px;color:#777">Vivamus sagittis lacus vel augue laoreet rutrum faucibus dolor auctor. Fusce dapibus, tellus ac cursus commodo, tortor mauris condimentum nibh, ut fe</p>
<div class="abs btn" style="left:91px;top:886px;width:54px;height:18px">View All</div>
<div class="abs gal ph" style="left:307px;background:linear-gradient(135deg,#1d1d22,#050505)" role="img" aria-label="Choir performing on a dark stage"></div>
<div class="abs gal ph" style="left:456px;background:linear-gradient(135deg,#5a2626,#2a1616)" role="img" aria-label="Choir members seated in a red room"></div>
<div class="abs gal" style="left:606px;background:linear-gradient(135deg,#e6cfa8,#c9ad82)" role="img" aria-label="Vintage choir emblem on aged paper"></div>
<div class="abs line" style="left:89px;top:922px;width:646px"></div>

<footer class="abs footer">
  <h3 style="left:90px;top:30px">Flickr Photostream</h3>
  <div class="abs thumb" style="left:90px;top:53px"></div><div class="abs thumb" style="left:138px;top:53px"></div><div class="abs thumb" style="left:186px;top:53px"></div>
  <div class="abs thumb" style="left:90px;top:101px"></div><div class="abs thumb" style="left:138px;top:101px"></div><div class="abs thumb" style="left:186px;top:101px"></div>
  <div class="abs thumb" style="left:90px;top:149px"></div><div class="abs thumb" style="left:138px;top:149px"></div><div class="abs thumb" style="left:186px;top:149px"></div>

  <h3 style="left:261px;top:30px">Latest Tweets</h3>
  <div class="abs tweet" style="top:52px"><svg width="9" height="9"><circle cx="4.5" cy="4.5" r="4.5" fill="#fff"/></svg><div class="t">about 1 day</div>ago@NorthHarborP<br>Thx for the support man!</div>
  <div class="abs tweet" style="top:105px"><svg width="9" height="9"><circle cx="4.5" cy="4.5" r="4.5" fill="#fff"/></svg><div class="t">about 1 day</div>ago@NorthHarborP<br>Thx for the support man!</div>
  <div class="abs tweet" style="top:159px"><svg width="9" height="9"><circle cx="4.5" cy="4.5" r="4.5" fill="#fff"/></svg><div class="t">about 1 day</div>ago@NorthHarborP<br>Thx for the support man!</div>

  <h3 style="left:418px;top:28px">New Release Out Now</h3>
  <div class="abs ph" style="left:417px;top:52px;width:126px;height:74px;border:2px solid #fff" role="img" aria-label="Band promo photo of four musicians"></div>
  <h3 style="left:421px;top:153px">Newsletter</h3>
  <div class="abs" style="left:421px;top:175px;width:60px;height:15px;background:#fff;color:#999;font-size:7px;padding:4px 3px">Email..</div>
  <div class="abs btn" style="left:481px;top:175px;width:62px;height:15px;border-radius:0;font-family:'Bebas Neue',sans-serif;font-size:11px">SUBSCRIBE</div>

  <h3 style="left:592px;top:28px">Upcoming Shows</h3>
  <div class="abs show" style="top:58px"><div class="ph" role="img" aria-label="Concert stage lights"></div><div class="t">Jul &nbsp;&nbsp; Chicago, IL (US)<br>Maple Hall<br>Buy ticket</div></div>
  <div class="abs show" style="top:110px"><div class="ph" role="img" aria-label="Performer on stage"></div><div class="t">Jul &nbsp;&nbsp; Chicago, IL (US)<br>Maple Hall<br>Buy ticket</div></div>
  <div class="abs show" style="top:160px"><div class="ph" role="img" aria-label="Concert hall audience"></div><div class="t">Jul &nbsp;&nbsp; Chicago, IL (US)<br>Maple Hall<br>Buy ticket</div></div>

  <div class="abs" style="left:90px;top:211px;width:646px;height:1px;background:rgba(255,255,255,.25)"></div>
  <div class="abs" style="left:90px;top:228px;font-size:8px">Copyright &copy; 2014 all rights are reserved</div>
</footer>
<div class="abs social" style="left:612px"></div>
<div class="abs social" style="left:638px"></div>
<div class="abs social" style="left:664px"></div>
<div class="abs social" style="left:689px"></div>
<div class="abs social" style="left:715px"></div>
</body>
</html>
```